【依頼の目的/概要】
電子書籍(lumora)の表紙デザインをお願いします。

【画像サイズ】※RXMより抜粋
表紙ファイルの理想的な寸法は2,560×1,600ピクセルです。
注:画像の寸法は1,000×625ピクセル以上であることが必要です。
画像の最大の寸法は10,000×10,000ピクセルです。

【タイトル】
黄金のレシピ
-10歳!本当の美しさに出会える魔法

【サブタイトル】
あなたは幸せ顔?診断テストが満載!
症状別に冷え・食・香りで解決!

【著者】
美容経歴20年以上・小学生~80歳のお悩み解決5000人以上
トータル美容アドバイザー:森川ゆかり(ブルームリーフ代表)

【本の内容】
この本は食生活・隠れ冷えなどを改善し、精油の力で美容健康に
導く本です。
ご自分の今の状態が解り、それぞれの不調・悩みを改善する
診断テストが盛りだくさんです。
以下に本の目次を書き出しました。
原稿も添付ファイルしますので宜しくお願いします。

第1章|真の美しさを引き出す土台づくり
◆気・血・水のバランスを整える
◆気・血・水のタイプ別:特徴
◆気・血・水のタイプ別:改善策
◆木・火・土・金・水
五行説で心身の弱点を診断
◆五行の診断テスト
◆五行別:改善策

第2章|美肌になるための食べ物
◆腸内環境を整えるオススメ食品
◆美肌になる食べ物

第3章|隠れ冷えを改善して、免疫力UP
◆あなたの体の「冷え」はどのタイプ?
◆各タイプ別:改善策

第4章|今日から簡単に取り入れられる!
お悩み別!美容の裏ワザQ&A
◆Q1:かかとのガサガサ、どうにかしたい!
◆Q2:何だか最近、顔がくすんでみえます・・・
◆Q3:お顔のたるみ、年のせいだから仕方ない?
◆Q4:爪が割れやすくなってきました・・・
◆Q5:お肌の乾燥が気になります!
◆Q6:タルミに効果的なマッサージは?
◆Q7:冬の紫外線対策って必要ですか?
◆Q8:年々、白髪や薄毛が気になります・・・
◆Q9:マスカラをキレイに塗りたい!
◆Q10:眉を早くキレイに描きたい!
◆Q11:正しいクレンジング方法は?

第5章|香りのある暮らし
精油の活用法&最新情報
◆皮脳同根の原理で脳ストレスを減らそう
◆精油を買う時のポイント
◆好きな香りで作る芳香剤
◆更年期にオススメの精油活用法
◆吸収のメカニズム・香りの経路
◆レジリエンスを高める4つのレッスン
◆あなたにぴったりな香りはどれ?
◆知られざる精油の効果・効能

【デザイン要望】
表紙のイラストは添付しますので、そのイラストを
使ってください。(ミストの女性)

デザインはご自由な発想でお願いします。

文字はタイトル、サブタイトル、著者を入れてください。

次点・次々点の方への参加報酬を設定いたしました。
ご応募を楽しみにお待ちしております。
その他何かご不明な点がございましたら、お気軽にご質問下さい。
よろしくお願いいたします。

この度は素晴らしいデザインをして頂きありがとうございました。
一目でパッと目につき、タイトル文字もはっきりしていて優しい
色合いにとても惹かれました。
何度も修正して頂きありがとうございます。

皆様、この度は素晴らしい沢山のご提案をありがとうございました。
お一人お一人にお礼を申し上げることができませんが、この場をお借りして
お礼申し上げます。本当に皆様お忙しい中ありがとうございました。

```html
<!DOCTYPE html>
<html lang="ja">
<head>
<meta charset="utf-8">
<title>黄金のレシピ</title>
<link rel="stylesheet" href="https://fonts.googleapis.com/css2?family=Cormorant+Garamond:wght@500&family=M+PLUS+Rounded+1c:wght@500;700;800&family=Noto+Sans+JP:wght@400;500;700&display=swap">
<style>
:root{
  --bg-top:#fde9ee;
  --bg-bottom:#f7c9d4;
  --magenta:#e2457c;
  --magenta-deep:#d12f6b;
  --ink:#4a4a4a;
  --ink-soft:#666;
  --script:#f2b3c3;
  --white:#ffffff;
  --badge:#ef6f98;
}
*{margin:0;padding:0;box-sizing:border-box}
html,body{width:750px;height:1200px;overflow:hidden}
body{font-family:"Noto Sans JP",sans-serif;color:var(--ink)}
.cover{position:relative;width:750px;height:1200px;overflow:hidden;
  background:linear-gradient(180deg,var(--bg-top) 0%,#fbdde5 45%,var(--bg-bottom) 100%)}
.bokeh{position:absolute;border-radius:50%;background:rgba(255,255,255,.55)}
.series{position:absolute;top:4px;left:0;width:100%;text-align:center;
  font-family:"Cormorant Garamond",serif;font-size:44px;letter-spacing:3px;color:var(--script)}
.title{position:absolute;top:28px;left:18px;font-family:"M PLUS Rounded 1c",sans-serif;font-weight:800;
  color:var(--magenta);white-space:nowrap;line-height:1;text-shadow:0 2px 0 rgba(255,255,255,.6)}
.title .big{font-size:120px}
.title .small{font-size:100px}
.tagline-age{position:absolute;top:240px;left:44px;font-family:"M PLUS Rounded 1c",sans-serif;
  font-weight:800;font-size:62px;color:var(--magenta-deep);line-height:1;white-space:nowrap}
.tagline{position:absolute;top:232px;left:300px;font-family:"M PLUS Rounded 1c",sans-serif;
  font-weight:700;font-size:48px;line-height:1.18;color:var(--ink);white-space:nowrap}
.tagline .accent{color:var(--magenta-deep)}
.illustration{position:absolute;left:270px;top:560px;width:480px;height:640px;
  background:radial-gradient(ellipse at 55% 45%,#fff3f0 0%,#fbe0e4 45%,#f3bfcc 100%);
  border-radius:240px 0 0 0}
.author{position:absolute;top:368px;left:24px;line-height:1.25}
.author .role{font-size:20px;font-weight:500;color:var(--ink)}
.author .name{font-family:"M PLUS Rounded 1c",sans-serif;font-size:42px;font-weight:800;color:var(--magenta-deep)}
.author .org{font-size:20px;color:var(--ink)}
.author .career{margin-top:14px;font-size:20px;line-height:1.35;color:var(--ink-soft)}
.bubble{position:absolute;border-radius:50%;display:flex;flex-direction:column;align-items:center;
  justify-content:center;text-align:center;font-family:"M PLUS Rounded 1c",sans-serif;font-weight:700}
.bubble-solve{left:470px;top:370px;width:270px;height:270px;background:var(--white);
  font-size:34px;line-height:1.3;color:var(--ink);box-shadow:0 0 30px rgba(255,255,255,.8)}
.bubble-solve .accent{color:var(--magenta-deep);font-size:32px}
.bubble-face{left:62px;top:585px;width:210px;height:210px;background:var(--white);
  font-size:34px;line-height:1.35;color:var(--ink);box-shadow:0 0 24px rgba(255,255,255,.8)}
.badge{left:6px;top:905px;width:240px;height:240px;background:var(--badge);
  color:var(--white);font-size:44px;line-height:1.2;font-weight:800}
</style>
</head>
<body>
<main class="cover">
  <span class="bokeh" style="left:-40px;top:-30px;width:240px;height:240px"></span>
  <span class="bokeh" style="left:560px;top:-60px;width:260px;height:260px"></span>
  <span class="bokeh" style="left:320px;top:120px;width:150px;height:150px;opacity:.6"></span>
  <span class="bokeh" style="left:560px;top:640px;width:120px;height:120px;opacity:.5"></span>

  <p class="series">Golden Recipe</p>
  <h1 class="title"><span class="big">黄金</span><span class="small">のレシピ</span></h1>
  <p class="tagline-age">−10歳!</p>
  <p class="tagline">本当の美しさに<br>出会える<span class="accent">魔法</span></p>

  <div class="illustration" role="img" aria-label="ミストを顔に吹きかける長い髪の女性のイラスト"></div>

  <section class="author">
    <p class="role">トータル美容アドバイザー</p>
    <p class="name">森川ゆかり</p>
    <p class="org">(ブルームリーフ代表)</p>
    <p class="career">美容経歴 20年以上<br>小学生〜80歳の<br>お悩み解決 5000人以上</p>
  </section>

  <div class="bubble bubble-solve"><span>症状別に</span><span class="accent">冷え・食・香り</span><span>で解決!</span></div>
  <div class="bubble bubble-face"><span>あなたは</span><span>幸せ顔?</span></div>
  <div class="bubble badge"><span>診断</span><span>テストが</span><span>満載!</span></div>
</main>
</body>
</html>
```